Criação de Manual da Marca para Consultoria de Negócios
" Serviço de assinatura de informações para postos de combustíveis, em um mercado onde centavos são relevantes, a plataforma lumitra vendas vem ao encontro de atender o processo de precificação para os donos, gestores de postos de combustíveis. "

```html
<!DOCTYPE html>
<html lang="pt-BR">
<head>
<meta charset="utf-8">
<title>Manual da Marca — lumitra vendas</title>
<link rel="stylesheet" href="https://fonts.googleapis.com/css2?family=Audiowide&family=Open+Sans:wght@400;600;700;800&display=swap">
<style>
  :root {
    --navy: #003763;
    --navy-dark: #0b2a4a;
    --orange: #ff6600;
    --paper: #f4f4f5;
    --ink: #1f2d3d;
    --muted: #6b7480;
    --stage: #e4e4e4;
    --display: "Audiowide", sans-serif;
    --body: "Open Sans", sans-serif;
  }
  * { box-sizing: border-box; margin: 0; padding: 0; }
  html, body { width: 1200px; height: 1200px; overflow: hidden; }
  body { background: var(--stage); font-family: var(--body); color: var(--ink); position: relative; }

  .spread { position: absolute; left: 48px; top: 290px; width: 1104px; height: 660px; display: flex; box-shadow: 0 12px 30px rgba(0,0,0,.18); }
  .page { position: relative; width: 552px; height: 660px; background: var(--paper); overflow: hidden; }
  .page--left { background: linear-gradient(90deg, var(--paper) 85%, #e2e3e6 100%); }
  .page--right { background: linear-gradient(90deg, #e2e3e6 0%, var(--paper) 15%); }
  .page-art { position: absolute; inset: 0; width: 100%; height: 100%; }

  .page-number { position: absolute; top: 70px; font: 800 30px/1 var(--body); color: var(--orange); }
  .page--left .page-number { left: 16px; }
  .page--right .page-number { left: 18px; }
  .intro { position: absolute; top: 52px; font-size: 8.5px; line-height: 1.45; color: var(--ink); }
  .page--left .intro { left: 70px; width: 440px; }
  .page--right .intro { left: 62px; width: 450px; }

  .section-title { position: absolute; font: 800 24px/1 var(--body); color: var(--navy); padding-left: 10px; border-left: 4px solid var(--orange); letter-spacing: .5px; }
  .page--left .section-title { left: 70px; top: 156px; }
  .page--right .section-title { left: 62px; top: 156px; }

  .copy { position: absolute; font-size: 9px; line-height: 1.5; color: var(--muted); }
  .copy p + p { margin-top: 12px; }
  .colors-copy { left: 70px; top: 200px; width: 160px; }

  .swatch { position: absolute; left: 270px; display: flex; align-items: center; gap: 10px; }
  .swatch-chip { width: 44px; height: 44px; }
  .swatch-chip--navy { background: var(--navy); }
  .swatch-chip--orange { background: var(--orange); }
  .swatch-code { font: 600 10px/1.35 var(--body); color: var(--ink); }
  .swatch--navy { top: 198px; }
  .swatch--orange { top: 254px; }

  .ramp { position: absolute; left: 270px; width: 168px; display: flex; flex-direction: column; gap: 2px; }
  .ramp span { display: block; height: 6px; }
  .ramp--navy { top: 320px; }
  .ramp--orange { top: 430px; }

  .brand-seal { position: absolute; left: 70px; top: 420px; display: flex; align-items: center; gap: 8px; }
  .brand-seal-dot { width: 22px; height: 22px; border-radius: 50%; background: var(--navy); }
  .brand-seal-name { font: 400 15px/1 var(--display); color: var(--navy); }

  .type-copy { left: 62px; top: 196px; width: 440px; }
  .type-name { position: absolute; left: 62px; top: 232px; font: 400 17px/1 var(--display); color: var(--orange); }
  .type-alphabet { position: absolute; left: 62px; top: 256px; width: 450px; font: 400 29px/1.15 var(--display); color: var(--navy); letter-spacing: .5px; }
  .type-note { position: absolute; left: 62px; font-size: 8.5px; color: var(--muted); }
  .type-note--a { top: 340px; }
  .type-digits { position: absolute; left: 62px; top: 370px; font: 400 30px/1 var(--display); color: var(--navy); letter-spacing: 1px; }
  .type-note--b { top: 418px; }
  .type-weights { position: absolute; left: 62px; top: 436px; width: 440px; display: grid; grid-template-columns: repeat(4, auto); justify-content: start; gap: 6px 16px; font: 400 18px/1 var(--display); }
  .w-navy { color: var(--navy); }
  .w-orange { color: var(--orange); }
  .w-pale { color: #f6b98f; }
  .w-small { font-size: 14px; align-self: end; }
  .observation { left: 62px; top: 510px; width: 440px; font-size: 8.5px; }
  .observation strong { color: var(--navy); }

  .footer-brand { position: absolute; left: 0; right: 0; top: 1060px; text-align: center; font: 400 30px/1 var(--display); color: var(--orange); }
</style>
</head>
<body>
  <main class="spread">
    <section class="page page--left">
      <svg class="page-art" viewBox="0 0 552 660" preserveAspectRatio="none" aria-hidden="true">
        <polygon points="0,0 130,0 70,26 0,26" fill="var(--navy)"/>
        <polygon points="130,0 175,0 105,26 70,26" fill="var(--orange)"/>
        <polygon points="0,26 70,26 0,56" fill="var(--navy-dark)"/>
        <polygon points="0,600 552,600 552,624 0,640" fill="var(--orange)"/>
        <polygon points="0,640 552,624 552,660 0,660" fill="var(--navy)"/>
      </svg>
      <div class="page-number">06</div>
      <p class="intro">Lorem Ipsum is simply dummy text of the printing and typesetting industry. Lorem Ipsum has been the industry's standard dummy text ever since the 1500s, when an unknown printer took a galley of type and scrambled it to make a type specimen book. It has survived not only five centuries, but also the leap into electronic typesetting, remaining essentially unchanged.</p>
      <h2 class="section-title">CORES</h2>
      <div class="copy colors-copy">
        <p>As cores principais garantem o reconhecimento da marca e criam distinção clara entre as empresas do segmento. São elas: azul e laranja.</p>
        <p>As secundárias são cores de apoio, usadas em peças de conteúdo, sempre em equilíbrio com as principais.</p>
        <p>Os degradês servem de fundo e reforçam a identidade em aplicações amplas da marca.</p>
      </div>
      <div class="swatch swatch--navy">
        <div class="swatch-chip swatch-chip--navy"></div>
        <div class="swatch-code">CMYK: 100.84.34.26<br>RGB: 0.55.99<br>HEX: #003763</div>
      </div>
      <div class="swatch swatch--orange">
        <div class="swatch-chip swatch-chip--orange"></div>
        <div class="swatch-code">CMYK: 0.74.100.0<br>RGB: 255.102.0<br>HEX: #FF6600</div>
      </div>
      <div class="ramp ramp--navy">
        <span style="background:#e6ebf1"></span><span style="background:#c7d3e0"></span><span style="background:#a4b8cc"></span><span style="background:#7f9ab6"></span><span style="background:#5a7c9f"></span><span style="background:#355f88"></span><span style="background:#1a4874"></span><span style="background:#003763"></span><span style="background:#003763;height:26px"></span>
      </div>
      <div class="ramp ramp--orange">
        <span style="background:#ffe9da"></span><span style="background:#ffd2b3"></span><span style="background:#ffb98a"></span><span style="background:#ff9f5f"></span><span style="background:#ff8535"></span><span style="background:#ff6600;height:26px"></span>
      </div>
      <div class="brand-seal">
        <span class="brand-seal-dot"></span>
        <span class="brand-seal-name">lumitra vendas</span>
      </div>
    </section>

    <section class="page page--right">
      <svg class="page-art" viewBox="0 0 552 660" preserveAspectRatio="none" aria-hidden="true">
        <polygon points="552,0 420,0 480,26 552,26" fill="var(--navy)"/>
        <polygon points="420,0 375,0 445,26 480,26" fill="var(--orange)"/>
        <polygon points="552,26 480,26 552,56" fill="var(--navy-dark)"/>
        <polygon points="280,660 552,600 552,660" fill="var(--orange)"/>
        <polygon points="400,660 552,626 552,660" fill="var(--navy)"/>
      </svg>
      <div class="page-number">07</div>
      <p class="intro">Lorem Ipsum is simply dummy text of the printing and typesetting industry. Lorem Ipsum has been the industry's standard dummy text ever since the 1500s, when an unknown printer took a galley of type and scrambled it to make a type specimen book. It has survived not only five centuries, but also the leap into electronic typesetting.</p>
      <h2 class="section-title">TIPOGRAFIA</h2>
      <p class="copy type-copy">A tipografia reforça a identidade visual e deve ser usada em títulos, destaques e chamadas curtas de todas as peças.</p>
      <div class="type-name">VELTRIX</div>
      <div class="type-alphabet">ABCDEFGHIJLMNOPQRS<br>TUVXZ</div>
      <p class="type-note type-note--a">Tipografia utilizada nos títulos, logotipo e chamadas principais.</p>
      <div class="type-digits">1234567890</div>
      <p class="type-note type-note--b">Tipografia utilizada para o texto de apoio das legendas: CONDENSADA E SEMICONDENSADA</p>
      <div class="type-weights">
        <span class="w-navy">VELTRIX</span><span class="w-orange">VELTRIX</span><span class="w-navy">VELTRIX</span><span class="w-orange w-small">VELTRIX</span>
        <span class="w-pale">VELTRIX</span><span class="w-pale">VELTRIX</span><span class="w-pale">VELTRIX</span><span class="w-pale w-small">VELTRIX</span>
      </div>
      <p class="copy observation"><strong>Observação:</strong> em títulos longos, prefira a versão condensada e mantenha o contraste entre as cores da marca.</p>
    </section>
  </main>

  <div class="footer-brand">lumitra vendas</div>
</body>
</html>
```